Modern Can & Tray Design Competition

Please note our brand is now called zé, please do not submit any entries with the wording or logo of "zé kelpwater". Read the full design brief below before making an entry, please.

A competition to design can packaging and outer tray designs for a new exciting brand.

See examples of the design assets I want, below, including both a can and outer tray:

1. https://quillmarketgoods.eu/beverages/energy-drinks/vomba-boost-the-amber-edition-12-x-025-liter-cans-nl/?lang=en

2. https://www.plimvo.com/nl/nl/p/tarvo-fizz-cherry-slim-cans-24-x-330-ml-eu/4812000077312904/

We have 2 flavours in our range, so we need two separate can designs and a separate outer tray design for each flavour.

Our drinks are currently packaged in PET plastic bottles. Our flavours are:
Lemon & Lime - https://zekelpwater.co.uk/products/lemon-and-lime
Strawberry - https://zekelpwater.co.uk/products/strawberry

For this competition, I want can designs for each flavour in 250ml style cans like used by Vomba. And I also want an outer tray for the cans designed for each flavour. Our brand is changing to “zé” so please do not use “kelpwater” on any part of the design. The logo should be “zé” and for each flavour the ze should show the fruit for the flavour embedded inside it. See the files called “ze_fruit_logo_LEMLI (1)” and “ze_fruit_logo_STR (1)” for what I mean. You can use these files for your design.

Under the logo it should state on the can “Prebiotic Fibre Drink”. Similar to how VomBa has “Energy Drink” written under its logo: https://www.drenvilo.com/wp-content/uploads/2009/11/vomba-can-250ml-1.jpg

If you can submit your design ideas for this competition with a picture of the can next to the tray like this for each flavour, that will be best: https://img.keltoshop.com/images/I/57qTzWa2pLx._SL1500_.jpg

So, two design concepts/ideas are needed to enter: One for Lemon & Lime and one for Strawberry.

We want vibrant, eye-catching packaging designs that will catch the consumer's attention.

Right now, we have ze in the centre of our packaging design with fruit embedded in the ze. This must remain a key part of your design as mentioned above. Also, as we will be launching other drinks as a company under different brand names and to unify our different brands we want a splash effect on all the cans which will be replicated across our other brands. So, please have some kind of splash effect on each flavour that can be replicated on the cans of our other brands in future.

Design considerations:

There is also certain information we need on the front/face of the can.

On the very top of the can just below the neck and above the logo we want it to state: “Supports Gut & Overall health*” example: https://pmkgrocerhub.co.uk/wp-content/uploads/2023/10/Brova-Zest-Lemonade.jpg

We also want the number of calories to be stated somewhere on the can in a clever way like in a droplet of the water splash effect. The number of the calories is “17 kcals”.

Under the ze logo as mentioned we want the wording: “Prebiotic Fibre Drink”

Then under Prebiotic Fibre Drink we want the name of the flavour - and then under the flavour we want 3 features stated. Which are:

“20% of daily fibre”
“0g sugar”
“Nothing artificial“

This could be laid out as 3 circles with icons or some other way. The last piece of information under these 3 features is then the size of the can “250 mle”.

In terms of “feel” of the design we want a vibrant colourful feel, and it should show pictures of fruit on it. Here is an example
https://gardenhollowtonics.com/wp-content/uploads/sites/2/2023/03/GHT-US-SodaRange-%E2%80%93-bb-1220x883.png

Any questions let me know. I look forward to seeing your ideas.

To see more about our brand, view our website: www.zekelpwater.co.uk

```html
<!DOCTYPE html>
<html lang="en">
<head>
<meta charset="utf-8">
<title>zé prebiotic fibre drink cans</title>
<link rel="stylesheet" href="https://fonts.googleapis.com/css2?family=Alfa+Slab+One&family=Open+Sans:wght@400;600&family=Oswald:wght@600&family=Quicksand:wght@500;700&display=swap">
<style>
  :root {
    --stage: #d2d2d2;
    --can-white: #f7f7f7;
    --can-edge: #e6e6e6;
    --lime-dark: #4f6e25;
    --lime-deep: #3f5a1f;
    --lime-mid: #6f9a35;
    --lime-brand: #7cbf3a;
    --lime-soft: #dde8b8;
    --lime-pale: #eef3c9;
    --berry-dark: #d8362f;
    --berry-mid: #e9564f;
    --berry-brand: #e23a33;
    --berry-soft: #f4c9bc;
    --berry-pale: #f9ddd2;
    --fibre-green: #5d7f2e;
  }
  html, body {
    margin: 0;
    width: 1200px;
    height: 1165px;
    overflow: hidden;
    background: var(--stage);
  }
  p { margin: 0; }
  .stage {
    position: relative;
    width: 1200px;
    height: 1165px;
  }
  .can {
    position: absolute;
    top: 92px;
    width: 380px;
    height: 976px;
    border-radius: 28px;
    background: linear-gradient(90deg, var(--can-edge) 0%, var(--can-white) 12%, #ffffff 50%, var(--can-white) 88%, var(--can-edge) 100%);
    overflow: hidden;
  }
  .can--lime { left: 174px; --ink: var(--lime-deep); --accent: var(--lime-mid); --brand: var(--lime-brand); --soft: var(--lime-soft); --pale: var(--lime-pale); --flavour: var(--lime-mid); }
  .can--berry { left: 612px; --ink: var(--berry-dark); --accent: var(--berry-mid); --brand: var(--berry-brand); --soft: var(--berry-soft); --pale: var(--berry-pale); --flavour: var(--berry-mid); }

  .can__backdrop { position: absolute; inset: 0; }

  .can__claim {
    position: absolute;
    top: 62px;
    left: 0;
    right: 0;
    text-align: center;
    font-family: 'Oswald', sans-serif;
    font-weight: 600;
    font-size: 18px;
    line-height: 22px;
    letter-spacing: 2.2px;
    text-transform: uppercase;
    color: var(--accent);
  }

  .can__brand {
    position: absolute;
    top: 130px;
    left: 0;
    right: 0;
    text-align: center;
    font-family: 'Quicksand', sans-serif;
    font-weight: 700;
    font-size: 250px;
    line-height: 1;
    color: var(--brand);
  }

  .can__fruit {
    position: absolute;
    left: 80px;
    top: 525px;
    width: 215px;
    height: 215px;
    border-radius: 50%;
  }
  .can--lime .can__fruit { background: radial-gradient(circle at 55% 50%, #d8e36a 0%, #a8c84a 35%, #4f6a2a 75%, rgba(79,106,42,0) 100%); }
  .can--berry .can__fruit { background: radial-gradient(circle at 55% 45%, #f6d3cc 0%, #ef5a4c 30%, #d52d2a 60%, rgba(213,45,42,0) 100%); }

  .kcal-drop {
    position: absolute;
    left: 60px;
    top: 600px;
    width: 64px;
    height: 64px;
    border-radius: 50% 50% 0 50%;
    background: var(--accent);
    color: #ffffff;
    font-family: 'Alfa Slab One', serif;
    text-align: center;
    display: flex;
    flex-direction: column;
    justify-content: center;
    line-height: 1;
  }
  .can--lime .kcal-drop { background: var(--lime-dark); }
  .kcal-drop__num { font-size: 24px; }
  .kcal-drop__unit { font-size: 13px; margin-top: 2px; }

  .can__flavour {
    position: absolute;
    top: 752px;
    left: 0;
    right: 0;
    text-align: center;
    font-family: 'Quicksand', sans-serif;
    font-weight: 500;
    font-size: 48px;
    line-height: 52px;
    color: var(--flavour);
  }
  .can__flavour .amp { font-size: 24px; }

  .can__type {
    position: absolute;
    top: 815px;
    left: 0;
    right: 0;
    text-align: center;
    font-family: 'Open Sans', sans-serif;
    font-size: 16px;
    line-height: 20px;
    color: var(--fibre-green);
  }

  .features {
    position: absolute;
    top: 860px;
    left: 0;
    right: 0;
    display: flex;
    justify-content: center;
    gap: 14px;
  }
  .feature {
    width: 44px;
    height: 44px;
    border-radius: 50%;
    background: var(--ink);
    color: #ffffff;
    font-family: 'Oswald', sans-serif;
    text-align: center;
    display: flex;
    flex-direction: column;
    justify-content: center;
    line-height: 1;
  }
  .feature--plain { background: var(--accent); }
  .feature__big { font-size: 14px; }
  .feature__small { font-family: 'Open Sans', sans-serif; font-size: 5px; margin-top: 1px; }
  .feature svg { display: block; margin: 0 auto; }

  .can__size {
    position: absolute;
    top: 932px;
    left: 0;
    right: 0;
    text-align: center;
    font-family: 'Alfa Slab One', serif;
    font-size: 24px;
    line-height: 28px;
    color: var(--ink);
  }
</style>
</head>
<body>
<main class="stage">

  <section class="can can--lime" aria-label="zé lime and lemon can">
    <svg class="can__backdrop" viewBox="0 0 380 976" aria-hidden="true">
      <path d="M42 85 C130 90 230 150 240 260 C250 360 160 390 90 350 C40 320 40 200 42 85 Z" fill="var(--soft)" opacity="0.7"/>
      <path d="M330 330 C300 450 330 620 270 760 C220 820 100 790 50 700 C20 620 40 470 120 440 C200 410 300 380 330 330 Z" fill="var(--pale)" opacity="0.9"/>
      <path d="M50 520 C120 500 250 540 290 640 C300 720 230 790 140 780 C60 760 40 640 50 520 Z" fill="var(--soft)" opacity="0.6"/>
    </svg>
    <p class="can__claim">Supports gut &amp; overall health</p>
    <div class="can__brand">zé</div>
    <div class="can__fruit" role="img" aria-label="Photo of a whole lime and halved lemons in a clear water splash"></div>
    <div class="kcal-drop"><span class="kcal-drop__num">17</span><span class="kcal-drop__unit">kcals</span></div>
    <p class="can__flavour">lime <span class="amp">&amp;</span>lemon</p>
    <p class="can__type">PREBIOTIC FIBRE DRINK</p>
    <div class="features">
      <div class="feature"><span class="feature__big">20%</span><span class="feature__small">of daily<br>fibre</span></div>
      <div class="feature"><span class="feature__big">0g</span><span class="feature__small">sugar</span></div>
      <div class="feature feature--plain" aria-label="Nothing artificial">
        <svg width="30" height="30" viewBox="0 0 30 30"><rect x="11" y="7" width="8" height="15" rx="2" fill="none" stroke="#fff" stroke-width="2"/><line x1="6" y1="24" x2="24" y2="6" stroke="#fff" stroke-width="2.5"/></svg>
      </div>
    </div>
    <p class="can__size">250ml</p>
  </section>

  <section class="can can--berry" aria-label="zé strawberry can">
    <svg class="can__backdrop" viewBox="0 0 380 976" aria-hidden="true">
      <path d="M42 75 C130 80 230 140 240 250 C250 350 160 380 90 340 C40 310 40 190 42 75 Z" fill="var(--pale)" opacity="0.9"/>
      <path d="M330 320 C300 440 330 620 270 770 C220 830 100 800 50 710 C20 620 40 470 120 440 C200 410 300 370 330 320 Z" fill="var(--pale)" opacity="0.9"/>
      <path d="M50 520 C120 490 250 530 290 640 C300 730 230 800 140 790 C60 770 40 640 50 520 Z" fill="var(--soft)" opacity="0.7"/>
    </svg>
    <p class="can__claim">Supports gut &amp; overall health</p>
    <div class="can__brand">zé</div>
    <div class="can__fruit" role="img" aria-label="Photo of a halved strawberry and a whole strawberry in a pink water splash"></div>
    <div class="kcal-drop"><span class="kcal-drop__num">17</span><span class="kcal-drop__unit">kcals</span></div>
    <p class="can__flavour">strawberry</p>
    <p class="can__type">PREBIOTIC FIBRE DRINK</p>
    <div class="features">
      <div class="feature"><span class="feature__big">20%</span><span class="feature__small">of daily<br>fibre</span></div>
      <div class="feature"><span class="feature__big">0g</span><span class="feature__small">sugar</span></div>
      <div class="feature feature--plain" aria-label="Nothing artificial">
        <svg width="30" height="30" viewBox="0 0 30 30"><rect x="11" y="7" width="8" height="15" rx="2" fill="none" stroke="#fff" stroke-width="2"/><line x1="6" y1="24" x2="24" y2="6" stroke="#fff" stroke-width="2.5"/></svg>
      </div>
    </div>
    <p class="can__size">250ml</p>
  </section>

</main>
</body>
</html>
```